Business Cards and Stationary For Home Automation Company
based on recently completed logo
Business Cards and Stationary For Home Automation Company  - Manufacturing
Creative Brief
Professional
Milo Brandt
VP - Product and Business Development
717 Larkfield Crest Avenue Suite K310 Piscataway, NJ 08821
milo@mybrightwaterdwellingtech.com
www.MyBrightwaterDwellingTech.com

```html
<!DOCTYPE html>
<html lang="en">
<head>
<meta charset="utf-8">
<title>Brightwater Dwelling Tech – Business Card</title>
<link href="https://fonts.googleapis.com/css2?family=Montserrat:wght@800&family=Open+Sans:wght@400;600&display=swap" rel="stylesheet">
<style>
  :root{
    --bg:#e9e9e7;
    --card:#f7f7f6;
    --ink:#141414;
    --muted:#6b6b6b;
    --green:#5fd12a;
    --rule:#c9c9c9;
  }
  *{box-sizing:border-box;margin:0;padding:0}
  html,body{width:1200px;height:901px;overflow:hidden;background:var(--bg)}
  .card{
    position:absolute;left:150px;top:190px;width:900px;height:520px;
    background:var(--card);border-radius:28px;overflow:hidden;
    box-shadow:0 10px 30px rgba(0,0,0,.18);
    font-family:"Open Sans",Arial,sans-serif;color:var(--ink);
  }
  .swoosh{position:absolute;left:0;top:0;width:900px;height:520px}
  .brand{position:absolute;left:70px;top:140px;display:flex;align-items:center;gap:18px}
  .brand-square{width:62px;height:62px;background:var(--ink);border-radius:6px}
  .brand-name{font-family:"Montserrat",Arial,sans-serif;font-weight:800;font-size:34px;line-height:1.02;color:var(--ink)}
  .tagline{position:absolute;left:72px;top:262px;font-size:13px;letter-spacing:5px;color:var(--muted);text-transform:uppercase}
  .divider{position:absolute;left:560px;top:44px;width:1px;height:250px;background:var(--rule)}
  .contact{position:absolute;left:582px;top:44px;width:300px}
  .contact-name{color:var(--green);font-size:20px;font-weight:600;letter-spacing:1px;text-transform:uppercase}
  .contact-title{color:var(--muted);font-size:14px;margin-top:2px}
  .contact-address{color:var(--ink);font-size:13px;line-height:1.45;margin-top:18px}
  .contact-lines{list-style:none;margin-top:16px}
  .contact-lines li{display:flex;align-items:center;gap:8px;font-size:12.5px;line-height:1.95;color:var(--ink)}
  .contact-lines svg{width:14px;height:14px;flex:none}
</style>
</head>
<body>
  <div class="card">
    <svg class="swoosh" viewBox="0 0 900 520" aria-hidden="true">
      <path d="M0 520 L0 478 C260 448 620 430 900 338 L900 520 Z" fill="#141414"/>
      <path d="M0 460 C260 430 600 412 900 300 L900 322 C610 428 270 448 0 472 Z" fill="#5fd12a"/>
    </svg>

    <div class="brand">
      <div class="brand-square"></div>
      <div class="brand-name">Brightwater<br>Dwelling<br>Tech</div>
    </div>
    <div class="tagline">Living Made Brighter</div>

    <div class="divider"></div>

    <div class="contact">
      <div class="contact-name">Milo Brandt</div>
      <div class="contact-title">Managing Director</div>
      <div class="contact-address">717 Larkfield Crest Avenue Suite K310<br>Piscataway, NJ 08821</div>
      <ul class="contact-lines">
        <li><svg viewBox="0 0 14 14"><circle cx="7" cy="7" r="7" fill="#5fd12a"/><path d="M4.5 3.5l1.6 1.6-.8 1a5 5 0 0 0 2.6 2.6l1-.8 1.6 1.6-.9 1C7 10.3 3.7 7 3.5 4.4z" fill="#fff"/></svg>555 014 2276</li>
        <li><svg viewBox="0 0 14 14"><circle cx="7" cy="7" r="7" fill="#5fd12a"/><rect x="5" y="3" width="4" height="8" rx="1" fill="#fff"/></svg>555 014 2277</li>
        <li><svg viewBox="0 0 14 14"><circle cx="7" cy="7" r="7" fill="#5fd12a"/><rect x="4" y="5" width="6" height="4" fill="#fff"/></svg>555 014 2278</li>
        <li><svg viewBox="0 0 14 14"><circle cx="7" cy="7" r="7" fill="#5fd12a"/><rect x="3.5" y="4.5" width="7" height="5" fill="#fff"/><path d="M3.5 4.5L7 7.3l3.5-2.8" stroke="#5fd12a" fill="none" stroke-width=".8"/></svg>milo@mybrightwaterdwellingtech.com</li>
        <li><svg viewBox="0 0 14 14"><circle cx="7" cy="7" r="7" fill="#5fd12a"/><circle cx="7" cy="7" r="3.5" fill="none" stroke="#fff" stroke-width="1"/><path d="M3.5 7h7M7 3.5v7" stroke="#fff" stroke-width=".8"/></svg>www.MyBrightwaterDwellingTech.com</li>
      </ul>
    </div>
  </div>
</body>
</html>
```